Business Card for Restaurant Zurimako

This project consist of creating 2 design for business card of restaurant named Nuvelo.

The attached specs below are 'ONLY SUGGESTION' if you have others ideas. You are welcome to post it.

1) Restaurant Card

Adresse:
2318 Rue des Pruniers
Montréal (Qc) H3K 2T8

Website:
www.nu-velo.ca

Phone:
438-552-0194

2) Employee Card

Name: Greta Lund
Title: Owner

Address:
2318 Rue des Pruniers
Montréal (Qc) H3K 2T8

Email:greta@nu-velo.ca
Phone Number:438-552-0194
Cellphone Number:514-730-4816

 The attached specs are 'ONLY SUGGESTION' if you have others ideas.  You are welcome to post it.

Industry/Entity Type

Restaurant

Requirements
Must have
• UV Card Spot

To print Spot UV business cards you would have to submit 2 files for each side. The first file "base" would be your regular design file as it would have been in any other case. The 2nd file "UV mask" is a black/white file. The BLACK color will indicate the areas that will be covered with the UV high gloss finish. To upload the files, please combine front design and front mask file in one P
Nice to have
• 1) The font of the logo should be ink effect
2) black background with wallpaper effect
3) The specs below are 'ONLY SUGGESTION' if you have others ideas. You are welcome to post it.

```html
<!DOCTYPE html>
<html lang="fr">
<head>
<meta charset="utf-8">
<title>Restaurant Zurimako – Cartes d'affaires</title>
<link rel="stylesheet" href="https://fonts.googleapis.com/css2?family=Roboto+Slab:wght@400;700&display=swap">
<style>
  :root {
    --backdrop: #3a3431;
    --card: #0e0e0e;
    --gloss: #262626;
    --ink: #f2f2f2;
    --muted: #8a8a8a;
    --red: #e0261b;
  }
  * { margin: 0; padding: 0; box-sizing: border-box; }
  html, body { width: 1200px; height: 716px; overflow: hidden; }
  body {
    background: var(--backdrop);
    font-family: "Roboto Slab", Georgia, serif;
    position: relative;
  }
  .card {
    position: absolute;
    top: 200px;
    width: 520px;
    height: 300px;
    background: var(--card);
    box-shadow: 0 12px 30px rgba(0,0,0,.45);
  }
  .card--front { left: 50px; }
  .card--back { left: 630px; }

  .brand { position: absolute; display: flex; align-items: center; gap: 12px; }
  .brand__name { font-weight: 700; line-height: 1; white-space: nowrap; }
  .brand__dot { border-radius: 50%; background: var(--red); flex: none; }
  .tagline { position: absolute; color: var(--muted); white-space: nowrap; }

  /* front: spot UV logo */
  .card--front .brand { left: 36px; top: 56px; }
  .card--front .brand__name { font-size: 76px; color: var(--gloss); }
  .card--front .brand__dot { width: 60px; height: 60px; }
  .card--front .tagline { left: 40px; top: 160px; font-size: 15px; }
  .website { position: absolute; right: 34px; bottom: 30px; color: var(--red); font-size: 18px; font-weight: 700; }

  /* back: contact side */
  .card--back .brand { left: 34px; top: 38px; }
  .card--back .brand__name { font-size: 44px; color: var(--ink); }
  .card--back .brand__dot { width: 34px; height: 34px; }
  .card--back .tagline { left: 36px; top: 98px; font-size: 10px; }

  .person { position: absolute; left: 36px; top: 148px; }
  .person__name { color: var(--red); font-size: 17px; text-transform: uppercase; }
  .person__title { color: var(--ink); font-size: 12px; }
  .field__label { color: var(--red); font-size: 11px; display: block; margin-top: 10px; }
  .field__value { color: var(--ink); font-size: 15px; }

  .address { position: absolute; left: 262px; top: 190px; color: var(--ink); font-size: 14px; line-height: 1.3; font-style: normal; }
  .phones { position: absolute; left: 262px; top: 234px; display: flex; gap: 24px; }
  .phones .field__label { margin-top: 0; }
</style>
</head>
<body>
  <section class="card card--front" aria-label="Recto">
    <div class="brand">
      <span class="brand__name">Zurimako</span>
      <span class="brand__dot"></span>
    </div>
    <p class="tagline">Resto-Bar Japonais • Izakaya • 居酒屋</p>
    <p class="website">www.nu-velo.ca</p>
  </section>

  <section class="card card--back" aria-label="Verso">
    <div class="brand">
      <span class="brand__name">Zurimako</span>
      <span class="brand__dot"></span>
    </div>
    <p class="tagline">Resto-Bar Japonais • Izakaya • 居酒屋</p>

    <div class="person">
      <p class="person__name">Greta Lund</p>
      <p class="person__title">Owner</p>
      <span class="field__label">email:</span>
      <span class="field__value">greta@nu-velo.ca</span>
    </div>

    <address class="address">2318 Rue des Pruniers<br>Montréal (Qc) H3K 2T8</address>

    <div class="phones">
      <div class="field">
        <span class="field__label">cell:</span>
        <span class="field__value">514-730-4816</span>
      </div>
      <div class="field">
        <span class="field__label">ph:</span>
        <span class="field__value">438-552-0194</span>
      </div>
    </div>
  </section>
</body>
</html>
```